Business Card Design

Please see my website www.lqvesting.com.au to for further information on my services and styling of my site

Project Deadline Extended
Reason: Deadline is extended to permit alterations to current designs or for any new submissions. Cheers

Industry/Entity Type

Business

Contact Information for Business Card

Marcus Theale
Empowerment Coach

'Live your passion'

marcus@lqvcoaching.com.au
0437518264
lqvcoaching.com.au

```html
<!DOCTYPE html>
<html lang="en">
<head>
<meta charset="UTF-8">
<title>Marcus Theale – Business Card</title>
<link rel="stylesheet" href="https://fonts.googleapis.com/css2?family=Bowlby+One&family=Open+Sans:wght@400;600&display=swap">
<style>
  :root {
    --page-bg: #e9e7e3;
    --card-bg: #f7f7f6;
    --card-shade: #e6e6e4;
    --brand-green: #94c13d;
    --brand-green-light: #a9cf5a;
    --ink-white: #ffffff;
    --ink-grey: #6f6f6f;
    --rule-grey: #9a9a9a;
  }
  * { margin: 0; padding: 0; box-sizing: border-box; }
  html, body {
    width: 1200px;
    height: 1023px;
    overflow: hidden;
    background: var(--page-bg);
    font-family: "Open Sans", Arial, sans-serif;
  }
  .card {
    position: absolute;
    left: 150px;
    top: 254px;
    width: 900px;
    height: 514px;
    background: linear-gradient(135deg, var(--ink-white) 0%, var(--card-bg) 55%, var(--card-shade) 100%);
    box-shadow: 0 10px 30px rgba(0,0,0,0.18);
  }
  .contact-band {
    position: absolute;
    left: 430px;
    top: 46px;
    right: 0;
    height: 212px;
    border-radius: 20px 0 0 20px;
    background: linear-gradient(180deg, var(--brand-green-light) 0%, var(--brand-green) 100%);
    color: var(--ink-white);
    padding: 34px 0 0 120px;
  }
  .contact-name {
    font-family: "Bowlby One", "Arial Black", sans-serif;
    font-size: 34px;
    letter-spacing: 1px;
    text-transform: uppercase;
    line-height: 1;
  }
  .contact-role {
    font-size: 17px;
    margin-top: 8px;
  }
  .contact-tagline {
    font-size: 16px;
    margin-top: 2px;
  }
  .contact-details {
    list-style: none;
    margin-top: 18px;
    font-size: 15px;
    line-height: 24px;
  }
  .contact-details li {
    display: flex;
    align-items: center;
    gap: 8px;
  }
  .contact-details svg { width: 14px; height: 14px; flex: none; }
  .brand {
    position: absolute;
    left: 110px;
    bottom: 92px;
    display: flex;
    align-items: center;
    gap: 14px;
    padding-bottom: 12px;
    border-bottom: 2px solid var(--rule-grey);
  }
  .brand-dot {
    width: 40px;
    height: 40px;
    border-radius: 50%;
    background: var(--brand-green);
  }
  .brand-name {
    font-size: 30px;
    font-weight: 400;
    color: var(--brand-green);
  }
</style>
</head>
<body>
  <main class="card">
    <section class="contact-band">
      <h1 class="contact-name">Marcus Theale</h1>
      <p class="contact-role">Empowerment Coach</p>
      <p class="contact-tagline">'Live your passion'</p>
      <ul class="contact-details">
        <li>
          <svg viewBox="0 0 14 14" aria-hidden="true"><rect x="3" y="1" width="8" height="12" rx="1.5" fill="none" stroke="#fff" stroke-width="1.5"/><circle cx="7" cy="10.5" r="0.9" fill="#fff"/></svg>
          0437518264
        </li>
        <li>
          <svg viewBox="0 0 14 14" aria-hidden="true"><rect x="1" y="3" width="12" height="8" fill="none" stroke="#fff" stroke-width="1.5"/><path d="M1 3 L7 8 L13 3" fill="none" stroke="#fff" stroke-width="1.5"/></svg>
          marcus@lqvcoaching.com.au
        </li>
        <li>
          <svg viewBox="0 0 14 14" aria-hidden="true"><circle cx="7" cy="7" r="5.5" fill="none" stroke="#fff" stroke-width="1.5"/><path d="M1.5 7 H12.5 M7 1.5 C4 5 4 9 7 12.5 M7 1.5 C10 5 10 9 7 12.5" fill="none" stroke="#fff" stroke-width="1"/></svg>
          lqvcoaching.com.au
        </li>
      </ul>
    </section>
    <div class="brand">
      <span class="brand-dot" aria-hidden="true"></span>
      <span class="brand-name">Vital Living Coaching</span>
    </div>
  </main>
</body>
</html>
```